Specialised investor in e-mobility and energy wants business card design

We need a business card design that fits our existing corporate design. <The look and feel must be 'sharp'/'clean', dynamic, communicate momentum, professionalism etc (as one would imagine from a firm in the financial sector). We like the idea of a reverse-side of the card that includes the logo, and the name and contact details on the other. We expect the deliverable to be whatever format might be required to be able to get cards printed directly by a service such as tandor press. Our website is www.orm.capital

```html
<!DOCTYPE html>
<html lang="en">
<head>
<meta charset="utf-8">
<title>ORM Capital – Business Card</title>
<link rel="stylesheet" href="https://fonts.googleapis.com/css2?family=Montserrat:wght@400;500;700;800&display=swap">
<style>
  :root {
    --backdrop: #dfe1e1;
    --paper: #f4f4f3;
    --green-deep: #1d3f16;
    --green-dark: #214c1b;
    --green-light: #6aa83a;
    --ink: #3a3a3a;
    --shadow: 0 14px 30px rgba(0,0,0,0.18);
  }
  * { box-sizing: border-box; margin: 0; padding: 0; }
  html, body {
    width: 1200px; height: 905px; overflow: hidden;
    background: var(--backdrop);
    font-family: "Montserrat", sans-serif;
  }
  .sheet {
    width: 1200px; height: 905px;
    display: flex; align-items: center; justify-content: center; gap: 40px;
  }
  .card {
    width: 520px; height: 298px;
    border-radius: 3px;
    box-shadow: var(--shadow);
    position: relative;
  }
  .card--front { background: var(--paper); }
  .card--back {
    background: var(--green-deep);
    display: flex; align-items: center; justify-content: center;
  }
  .wordmark {
    display: flex; align-items: center; gap: 10px;
    font-weight: 500; letter-spacing: 0.5px;
  }
  .wordmark__dot { border-radius: 50%; background: var(--green-light); flex: none; }
  .wordmark__name { color: var(--green-dark); }
  .card--front .wordmark { position: absolute; top: 40px; left: 0; right: 0; justify-content: center; font-size: 34px; }
  .card--front .wordmark__dot { width: 16px; height: 16px; }
  .card--back .wordmark { font-size: 48px; }
  .card--back .wordmark__name { color: #f1f1f1; }
  .card--back .wordmark__dot { width: 22px; height: 22px; }

  .holder { position: absolute; top: 114px; left: 0; right: 0; text-align: center; }
  .holder__name { font-size: 20px; font-weight: 800; letter-spacing: 1px; color: var(--green-dark); }
  .holder__name .surname { color: var(--green-light); }
  .holder__role { font-size: 13px; color: var(--ink); margin-top: 2px; }

  .details {
    position: absolute; top: 184px; left: 0; right: 0;
    display: flex; justify-content: center;
    font-size: 13px; color: var(--ink); line-height: 1.65;
  }
  .details__address { text-align: right; padding-right: 18px; padding-top: 2px; }
  .details__divider { width: 1px; background: var(--green-dark); align-self: stretch; }
  .details__contact { padding-left: 18px; list-style: none; }
  .details__contact li { display: flex; align-items: center; gap: 8px; }
  .details__contact svg { width: 12px; height: 12px; fill: var(--green-light); flex: none; }
</style>
</head>
<body>
<main class="sheet">
  <section class="card card--front" aria-label="Business card front">
    <div class="wordmark"><span class="wordmark__dot"></span><span class="wordmark__name">ORM Capital</span></div>
    <div class="holder">
      <p class="holder__name">MARCUS <span class="surname">FELDT</span></p>
      <p class="holder__role">Director/Founder</p>
    </div>
    <div class="details">
      <address class="details__address" style="font-style:normal">
        1234 Street Name<br>Country Name AB 5748
      </address>
      <span class="details__divider"></span>
      <ul class="details__contact">
        <li><svg viewBox="0 0 24 24" aria-hidden="true"><path d="M6.6 10.8a15.1 15.1 0 0 0 6.6 6.6l2.2-2.2a1 1 0 0 1 1-.25 11.4 11.4 0 0 0 3.6.57 1 1 0 0 1 1 1V20a1 1 0 0 1-1 1A17 17 0 0 1 3 4a1 1 0 0 1 1-1h3.5a1 1 0 0 1 1 1c0 1.25.2 2.45.57 3.57a1 1 0 0 1-.25 1z"/></svg>123-408-2931</li>
        <li><svg viewBox="0 0 24 24" aria-hidden="true"><path d="M2 5h20v14H2z M2 5l10 8 10-8" stroke="#f4f4f3" stroke-width="1.5"/></svg>info@orm.capital</li>
        <li><svg viewBox="0 0 24 24" aria-hidden="true"><circle cx="12" cy="12" r="10"/><path d="M2 12h20M12 2c3 3 3 17 0 20M12 2c-3 3-3 17 0 20" stroke="#f4f4f3" stroke-width="1.3" fill="none"/></svg>www.orm.capital</li>
      </ul>
    </div>
  </section>

  <section class="card card--back" aria-label="Business card back">
    <div class="wordmark"><span class="wordmark__dot"></span><span class="wordmark__name">ORM Capital</span></div>
  </section>
</main>
</body>
</html>
```